Save our Business Card - We need your help

We need a fresh look on our business cards. We like it as it is, but it's not quite getting the 'wow' effect that we desire.
We're a tech startup building a cloud based solution for retailers consisting of Point of Sale, Inventory management and CRM.
The design should communicate a sense of a company that cares about the little things, design and relationships.
You can have a look at our website www.tillnest.com to get a feel for what we're like. Please feel free to message us for any further clarification
Target Market(s)
Our Customers are retail busines owners, cafe owners, other startups etc.
Industry/Entity Type
Building
Colors
Designer to choose colors to be used in the design.
Look and feel
Each slider illustrates characteristics of the customer's brand and the style your logo design should communicate.

```html
<!DOCTYPE html>
<html lang="en">
<head>
<meta charset="utf-8">
<title>Tillnest Business Card</title>
<link rel="stylesheet" href="https://fonts.googleapis.com/css2?family=Didact+Gothic&family=Open+Sans:wght@700;800&display=swap">
<style>
  :root {
    --bg: #2b2b2b;
    --orange: #f0921e;
    --orange-deep: #e9861a;
    --white: #ffffff;
    --paper: #f7f7f7;
    --ink: #3a3a3a;
    --ink-soft: #555555;
  }
  * { box-sizing: border-box; margin: 0; padding: 0; }
  html, body {
    width: 1200px; height: 997px; overflow: hidden;
    background: var(--bg);
  }
  .stage { position: relative; width: 1200px; height: 997px; }

  .card {
    position: absolute;
    width: 560px; height: 320px;
    border-radius: 22px;
    overflow: hidden;
    box-shadow: 0 14px 30px rgba(0,0,0,.45);
  }

  /* Front */
  .card-front {
    left: 70px; top: 150px;
    background: linear-gradient(180deg, var(--orange) 0%, var(--orange-deep) 100%);
  }
  .front-band {
    position: absolute; left: 0; right: 0; top: 112px; height: 118px;
    background: var(--white);
  }
  .front-url {
    position: absolute; left: 56px; top: 92px;
    font: 700 15px "Open Sans", sans-serif; color: var(--ink);
  }
  .front-brand {
    position: absolute; left: 52px; top: 122px;
    font: 800 54px/1 "Open Sans", sans-serif; color: var(--orange);
    letter-spacing: -0.5px;
  }
  .front-tagline {
    position: absolute; left: 56px; top: 186px;
    font: 700 15px "Open Sans", sans-serif; color: var(--ink);
    letter-spacing: 0.5px;
  }
  .front-mark {
    position: absolute; right: 70px; top: 128px;
    width: 86px; height: 86px; background: var(--orange);
  }

  /* Back */
  .card-back {
    left: 570px; top: 470px;
    background: linear-gradient(135deg, var(--white) 0%, var(--paper) 100%);
  }
  .back-logo {
    position: absolute; right: 44px; top: 44px;
    display: flex; align-items: center; gap: 12px;
  }
  .back-logo-mark { width: 48px; height: 48px; background: var(--orange); }
  .back-logo-name {
    font: 800 34px/1 "Open Sans", sans-serif; color: var(--orange);
  }
  .holder {
    position: absolute; left: 44px; top: 150px;
    font-family: "Didact Gothic", sans-serif;
  }
  .holder-name { font-size: 24px; color: var(--orange); letter-spacing: 0.5px; }
  .holder-title { font-size: 19px; color: var(--ink-soft); margin-top: 2px; }

  .contacts {
    position: absolute; left: 44px; top: 226px; right: 30px;
    list-style: none;
    font: 17px/1 "Didact Gothic", sans-serif; color: var(--ink);
  }
  .contacts li { display: flex; align-items: center; gap: 10px; height: 27px; }
  .contacts svg { width: 18px; height: 18px; fill: var(--orange); flex: none; }
  .contact-web {
    position: absolute; left: 280px; top: 226px;
    display: flex; align-items: center; gap: 10px; height: 27px;
    font: 17px/1 "Didact Gothic", sans-serif; color: var(--ink);
  }
  .contact-web svg { width: 18px; height: 18px; fill: none; stroke: var(--orange); stroke-width: 2.4; }
</style>
</head>
<body>
<main class="stage">

  <section class="card card-front" aria-label="Card front">
    <div class="front-band"></div>
    <p class="front-url">www.tillnest.com</p>
    <h1 class="front-brand">Tillnest</h1>
    <p class="front-tagline">MAKES YOUR BUSINESS AWESOME</p>
    <div class="front-mark"></div>
  </section>

  <section class="card card-back" aria-label="Card back">
    <div class="back-logo">
      <div class="back-logo-mark"></div>
      <span class="back-logo-name">Tillnest</span>
    </div>

    <div class="holder">
      <p class="holder-name">YOUR NAME</p>
      <p class="holder-title">Designation</p>
    </div>

    <div class="contact-web">
      <svg viewBox="0 0 20 20"><path d="M8 12l4-4M9 5l2-2a3 3 0 014 4l-2 2M11 15l-2 2a3 3 0 01-4-4l2-2"/></svg>
      <span>www.quillbyte.net</span>
    </div>

    <ul class="contacts">
      <li>
        <svg viewBox="0 0 20 20"><path d="M2 6c0-2 3-3 8-3s8 1 8 3v2h-4V6H6v2H2zM5 9h10l2 7H3z"/></svg>
        <span>+1 555-014-2290</span>
      </li>
      <li>
        <svg viewBox="0 0 20 20"><path d="M10 2l8 7h-2v8h-4v-5H8v5H4V9H2z"/></svg>
        <span>71 Alder Lane Hollis Bay, Maine 04011</span>
      </li>
      <li>
        <svg viewBox="0 0 20 20"><path d="M2 5h16v10H2zM2 5l8 6 8-6" stroke="#fff" stroke-width="1.2"/></svg>
        <span>appointments@quillbyte.net</span>
      </li>
    </ul>
  </section>

</main>
</body>
</html>
```